Business cards for a high-end menswear store

I would like to come up with a design for our business cards.
Two different ones: one for general sales and one for the owner. It is a high-end menswear store.

Our address is: 4817 Morneau Boulevard, Montreal, QC, K7P4M2
phone number: 514-286-5937
insta: MAISONVERLAINE
Website: www.maisonverlaine.example
email (general card): info@maisonverlaine.example
email (owner): bastien@maisonverlaine.example

I have attached our logo in an ai and eps file format. You can see our old cards as well. I am looking for a modern and clean look.

Target Market(s)

High-End Clothing Market

Industry/Entity Type

Retail, Clothing, Luxury Clothing

Contact Information for Business Card

Address, Name, Email, Website, Social Info,

Font styles to use
Serif

Colors

Designer to choose colors to be used in the design.

Requirements
Must have
• Address, Name, Email, Website, Social Info,
Nice to have
• QR Code that brings you to the website

```html
<!DOCTYPE html>
<html lang="en">
<head>
<meta charset="utf-8">
<title>Maison Verlaine — Business Cards</title>
<link rel="stylesheet" href="https://fonts.googleapis.com/css2?family=Arimo:wght@400;500&family=Playfair+Display:wght@700&display=swap">
<style>
  :root {
    --backdrop: #8b8b8b;
    --ink: #1f1d1d;
    --paper: #ffffff;
    --text-light: #f2f2f2;
    --text-muted: #d6d6d6;
  }
  * { box-sizing: border-box; margin: 0; padding: 0; }
  html, body {
    width: 1200px; height: 960px; overflow: hidden;
    background: var(--backdrop);
  }
  .sheet {
    position: relative; width: 1200px; height: 960px;
  }
  .card {
    position: absolute; left: 250px; width: 700px; height: 400px;
    box-shadow: 0 6px 18px rgba(0,0,0,0.25);
    overflow: hidden;
  }
  .card--front { top: 60px; background: var(--ink); }
  .card--back { top: 500px; display: flex; }

  .brand {
    position: absolute; display: flex; flex-direction: column; align-items: center; gap: 14px;
  }
  .brand__square { width: 150px; height: 150px; }
  .brand__name {
    font-family: "Arimo", sans-serif; font-weight: 400;
    font-size: 15px; letter-spacing: 0.42em; text-transform: uppercase;
    padding-left: 0.42em;
  }
  .card--front .brand { left: 50%; top: 50%; transform: translate(-50%, -50%); }
  .card--front .brand__square { background: var(--paper); }
  .card--front .brand__name { color: var(--paper); }

  .back__logo-side {
    position: relative; width: 296px; height: 100%; background: var(--paper);
  }
  .back__logo-side .brand { left: 50%; top: 50%; transform: translate(-50%, -50%); }
  .back__logo-side .brand__square { background: var(--ink); width: 140px; height: 140px; }
  .back__logo-side .brand__name { color: var(--ink); font-size: 13px; }

  .back__info {
    flex: 1; background: var(--ink); color: var(--text-light);
    padding: 72px 0 0 52px;
    font-family: "Arimo", sans-serif;
  }
  .person__name {
    font-family: "Playfair Display", serif; font-weight: 700;
    font-size: 22px; letter-spacing: 0.04em; color: var(--paper);
  }
  .person__role { font-size: 15px; color: var(--text-muted); margin: 2px 0 22px 14px; }
  .address { font-size: 15px; line-height: 1.3; color: var(--text-light); margin: 0 0 18px 14px; }
  .contacts { list-style: none; font-size: 15px; }
  .contacts li { display: flex; align-items: center; gap: 10px; line-height: 1.45; }
  .contacts svg { width: 12px; height: 12px; flex: none; }
</style>
</head>
<body>
<main class="sheet">
  <section class="card card--front" aria-label="Card front">
    <div class="brand">
      <div class="brand__square"></div>
      <p class="brand__name">Maison Verlaine</p>
    </div>
  </section>

  <section class="card card--back" aria-label="Card back, owner">
    <div class="back__logo-side">
      <div class="brand">
        <div class="brand__square"></div>
        <p class="brand__name">Maison Verlaine</p>
      </div>
    </div>
    <div class="back__info">
      <h1 class="person__name">BASTIEN</h1>
      <p class="person__role">Owner</p>
      <p class="address">4817 Morneau Boulevard<br>Montreal, QC, K7P4M2</p>
      <ul class="contacts">
        <li>
          <svg viewBox="0 0 12 12" aria-hidden="true"><path fill="#fff" d="M2.5 1l2 2-1 1.3c.6 1.4 1.8 2.6 3.2 3.2L8 6.5l2 2-1 1.8C4.8 10 2 7.2 1 3.5z"/></svg>
          514-286-5937
        </li>
        <li>
          <svg viewBox="0 0 12 12" aria-hidden="true"><rect x="1" y="2.5" width="10" height="7" fill="#fff"/><path d="M1 2.5l5 4 5-4" fill="none" stroke="#1f1d1d" stroke-width="1"/></svg>
          bastien@maisonverlaine.example
        </li>
        <li>
          <svg viewBox="0 0 12 12" aria-hidden="true"><circle cx="6" cy="6" r="5" fill="none" stroke="#fff" stroke-width="1.2"/><path d="M1 6h10M6 1c-2.5 3-2.5 7 0 10M6 1c2.5 3 2.5 7 0 10" fill="none" stroke="#fff" stroke-width="0.9"/></svg>
          www.maisonverlaine.example
        </li>
        <li>
          <svg viewBox="0 0 12 12" aria-hidden="true"><circle cx="6" cy="6" r="4.5" fill="#fff"/></svg>
          MAISONVERLAINE
        </li>
      </ul>
    </div>
  </section>
</main>
</body>
</html>
```